Business Card Design for Harbourline Aerial

Hi we need a business card designed for a new aerial photography business we have started, we use UAV Drones to take photos for corporate, events, real estate, local government etc , the business name is Harbourline Aerial Co., we have a facebook page that might help you come up with some designs - https://www.facebook.com/loftpicturesaustralia

We need to have and editable AI file so that we can use different names and contact details. details for one of the cards as follow:

Ned Harrow
phone: 03 5521 4736
Mobile: 0431 957 284
email: ned@harbourline.example
web: www.harbourline.example

have now changed: Designer Payment:Committed

Target Market(s)

We are a Aerial Photography business using Drones and UAV

Industry/Entity Type

Business

Logo Text

Harbourline Aerial Co.

Requirements
Must have
• Colors to match logo and be part of Harbourline Aerial Brand

```html
<!DOCTYPE html>
<html lang="en">
<head>
<meta charset="utf-8">
<title>Harbourline Aerial Co. – Business Card</title>
<link rel="stylesheet" href="https://fonts.googleapis.com/css2?family=Montserrat:wght@700&family=Open+Sans:wght@400&family=Pinyon+Script&display=swap">
<style>
  :root {
    --stage: #c8c8c8;
    --card-light: #7a8f93;
    --card-mid: #6b8185;
    --card-dark: #56696d;
    --ink-light: #eef4f5;
    --ink-brand: #25292c;
    --shadow: rgba(0, 0, 0, 0.22);
  }
  * { box-sizing: border-box; margin: 0; padding: 0; }
  html, body {
    width: 1200px;
    height: 873px;
    overflow: hidden;
    background: var(--stage);
  }
  .stage {
    width: 1200px;
    height: 873px;
    display: flex;
    align-items: center;
    justify-content: center;
    gap: 60px;
  }
  .card {
    position: relative;
    width: 510px;
    height: 340px;
    overflow: hidden;
    box-shadow: 0 18px 30px var(--shadow);
  }
  .card__photo {
    position: absolute;
    inset: 0;
    background: linear-gradient(180deg, var(--card-light) 0%, var(--card-mid) 55%, var(--card-dark) 100%);
  }
  .card__content {
    position: absolute;
    inset: 0;
  }
  /* Front */
  .card--front .card__content {
    display: flex;
    flex-direction: column;
    align-items: center;
    justify-content: center;
  }
  .brand-name {
    font-family: "Montserrat", sans-serif;
    font-weight: 700;
    text-transform: uppercase;
    color: var(--ink-brand);
    text-align: center;
  }
  .brand-name__main {
    display: block;
    font-size: 36px;
    line-height: 1.1;
    letter-spacing: 1px;
  }
  .brand-name__sub {
    display: block;
    margin-top: 6px;
    font-size: 14px;
    letter-spacing: 9px;
  }
  /* Back */
  .holder-name {
    position: absolute;
    left: 44px;
    top: 70px;
    font-family: "Pinyon Script", cursive;
    font-weight: 400;
    font-size: 56px;
    color: var(--ink-light);
    white-space: nowrap;
  }
  .contact-list {
    position: absolute;
    left: 190px;
    top: 160px;
    list-style: none;
  }
  .contact-list__item {
    display: flex;
    align-items: center;
    gap: 10px;
    height: 26px;
    font-family: "Open Sans", sans-serif;
    font-size: 13px;
    color: var(--ink-light);
    white-space: nowrap;
  }
  .contact-list__icon {
    width: 16px;
    height: 16px;
    flex: none;
  }
</style>
</head>
<body>
<main class="stage">
  <section class="card card--front" aria-label="Business card front">
    <div class="card__photo" role="img" aria-label="Hazy aerial photograph of a city skyline across parkland"></div>
    <div class="card__content">
      <p class="brand-name">
        <span class="brand-name__main">Harbourline</span>
        <span class="brand-name__sub">Aerial Co.</span>
      </p>
    </div>
  </section>

  <section class="card card--back" aria-label="Business card back">
    <div class="card__photo" role="img" aria-label="Hazy aerial photograph of a city skyline across parkland"></div>
    <div class="card__content">
      <h1 class="holder-name">Ned Harrow</h1>
      <ul class="contact-list">
        <li class="contact-list__item">
          <svg class="contact-list__icon" viewBox="0 0 16 16" aria-hidden="true">
            <rect x="2" y="2" width="12" height="12" rx="1.5" fill="#eef4f5"/>
            <path d="M5 5h6v2H5zM5 9h1.5v1.5H5zM7.25 9h1.5v1.5h-1.5zM9.5 9H11v1.5H9.5z" fill="#6b8185"/>
          </svg>
          <span>03 5521 4736</span>
        </li>
        <li class="contact-list__item">
          <svg class="contact-list__icon" viewBox="0 0 16 16" aria-hidden="true">
            <rect x="4" y="1" width="8" height="14" rx="1.5" fill="none" stroke="#eef4f5" stroke-width="1.4"/>
            <circle cx="8" cy="12.5" r="0.9" fill="#eef4f5"/>
          </svg>
          <span>0431 957 284</span>
        </li>
        <li class="contact-list__item">
          <svg class="contact-list__icon" viewBox="0 0 16 16" aria-hidden="true">
            <rect x="1.5" y="3.5" width="13" height="9" fill="#eef4f5"/>
            <path d="M1.5 3.5 8 9l6.5-5.5" fill="none" stroke="#6b8185" stroke-width="1.1"/>
          </svg>
          <span>ned@harbourline.example</span>
        </li>
        <li class="contact-list__item">
          <svg class="contact-list__icon" viewBox="0 0 16 16" aria-hidden="true">
            <circle cx="8" cy="8" r="6.5" fill="#eef4f5"/>
            <path d="M1.5 8h13M8 1.5c-2.5 2.5-2.5 10.5 0 13M8 1.5c2.5 2.5 2.5 10.5 0 13" fill="none" stroke="#6b8185" stroke-width="0.9"/>
          </svg>
          <span>www.harbourline.example</span>
        </li>
      </ul>
    </div>
  </section>
</main>
</body>
</html>
```